Silverleaf Mobile Massage Business Needs a New Website

Hello,
We require a website to be designed and coded. The design and coding must be high quality. Our website host has requested files be in static HTML format if possible.

The business is a mobile massage service for seniors (elderly people). The designer should emphasise that the business is a mobile service

The website will only have 4 pages.

1. Home- very simple layout and minimal information
2. Massage Services- this houses all of the information about the different services etc.
3. Contact Us-
4. ホーム (this is the Japanese symbol for 'home')- All of the information on the home page (section 1) will be translated into Japanese and uploaded to the brief for the designers to insert.

There is no requirement for an online booking, just contact information. The words 'Make a Booking' can be used and should lead customers to the 'Contact Us' page.

I have attached the business logo in multiple formats for designers to use.

I will upload more content and images to use for the website by the end of this week.

Thank you. I look forward to working with the successful candidate.

Target Market(s)

People aged 50+ years

Industry/Entity Type

Massage Therapy

Coding

Coded - Design and coding required

Number of Pages Required

4 page

Font styles to use
Sans Serif

Colors
74cabd
abd036
9ccb3b
f6faec
ffffff

Requirements
Must have
• Copyright free images and photos that we have taken. Both are important.
• Simple and inviting design.
Nice to have
• Colours of the logo incorporated.
Should not have
• This business is not a massage shop, so no images of massage shops or day salons required.
• Not too much imagery as the design needs to be simple.

```html
<!DOCTYPE html>
<html lang="en">
<head>
<meta charset="utf-8">
<title>Silverleaf Mobile Massage</title>
<link href="https://fonts.googleapis.com/css2?family=Raleway:wght@400;600;700;800&family=Open+Sans:wght@400;600&family=Noto+Sans+JP:wght@400&display=swap" rel="stylesheet">
<style>
:root{
  --green:#9ccb3b;
  --lime:#abd036;
  --teal:#74cabd;
  --pale:#f6faec;
  --white:#ffffff;
  --ink:#333333;
  --text:#666666;
  --line:#dcdcdc;
  --dark:#1e1e1e;
}
*{box-sizing:border-box;margin:0;padding:0}
html,body{width:1200px;height:2960px;overflow:hidden}
body{font-family:"Open Sans",sans-serif;color:var(--text);background:var(--white);font-size:14px;line-height:1.6}
section,header,footer{position:relative;width:1200px}
.heading{font-family:"Raleway",sans-serif;font-variant:small-caps;font-weight:600;font-size:40px;color:var(--ink);text-align:center;letter-spacing:1px}
.heading .accent{color:var(--green)}
.btn{display:inline-block;font-family:"Raleway",sans-serif;font-weight:600;font-size:15px;padding:12px 26px;border-radius:3px;text-transform:uppercase}
.btn-green{background:var(--green);color:var(--white)}
.btn-dark{background:var(--dark);color:var(--white)}
.btn-white{background:var(--white);color:var(--ink)}
.ph{position:absolute}

/* top bar */
.topbar{height:32px;background:var(--white)}
.topbar .contact{position:absolute;right:0;top:0;height:32px;background:var(--green);color:var(--white);font-size:13px;display:flex;align-items:center;gap:28px;padding:0 40px 0 30px;border-bottom-left-radius:16px}
.topbar .contact span{display:flex;align-items:center;gap:8px}

/* header */
.site-header{height:96px;border-bottom:1px solid var(--line)}
.brand{position:absolute;left:40px;top:20px;display:flex;align-items:center;gap:14px}
.brand .dot{width:46px;height:46px;border-radius:50%;background:var(--green)}
.brand .name{font-family:"Raleway",sans-serif;font-weight:700;font-size:22px;color:var(--green);letter-spacing:1px;text-transform:uppercase}
.nav{position:absolute;right:40px;top:0;display:flex;height:96px}
.nav a{display:flex;align-items:center;padding:0 34px;font-family:"Raleway",sans-serif;font-weight:600;font-size:16px;color:var(--ink);text-transform:uppercase;border-top:4px solid transparent}
.nav a.active{color:var(--green);border-top-color:var(--green)}
.nav a.jp{font-family:"Noto Sans JP",sans-serif;font-weight:400}

/* hero */
.hero{height:572px;background:linear-gradient(100deg,#efe9e2 0%,#d9c2ab 45%,#c49878 70%,#e7d3bf 100%)}
.hero-text{position:absolute;left:70px;top:150px;font-family:"Raleway",sans-serif;color:var(--dark)}
.hero-text .small{font-size:32px;font-weight:700;text-transform:uppercase}
.hero-text .mid{font-size:44px;font-weight:800;text-transform:uppercase;line-height:1.1}
.hero-text .big{font-size:66px;font-weight:800;text-transform:uppercase;line-height:1.1;margin-bottom:34px}

/* welcome */
.welcome{height:440px}
.welcome .heading{padding-top:56px}
.welcome .copy{position:absolute;left:70px;top:150px;width:560px;font-size:15px}
.welcome .btn{position:absolute;left:70px;top:345px}
.welcome .photo{left:840px;top:120px;width:290px;height:260px;background:linear-gradient(135deg,#f3eee8,#d8b89c 55%,#f0e6dc)}

/* services */
.services{height:460px;background:var(--pale)}
.services .heading{padding-top:40px}
.tabs{position:absolute;left:340px;top:118px;display:flex;gap:22px;font-size:15px;color:var(--ink);border-bottom:1px solid var(--line)}
.tabs span{padding-bottom:6px}
.tabs span.active{border-bottom:3px solid var(--green)}
.services .photo{left:240px;top:170px;width:340px;height:250px;background:linear-gradient(135deg,#f2d4c4,#e5b49b 50%,#d4a3c8)}
.services .copy{position:absolute;left:620px;top:170px;width:400px;font-size:14px}
.services .copy p{margin-bottom:18px}

/* offer */
.offer{height:280px;background:var(--green);text-align:center}
.offer .heading{padding-top:34px}
.offer .deal{font-family:"Raleway",sans-serif;font-weight:600;font-size:52px;color:var(--white);line-height:1.3}
.offer .btn{margin-top:20px}

/* testimonials */
.testimonials{height:240px;border-bottom:1px solid var(--line)}
.quote{position:absolute;top:60px;width:460px;display:flex;gap:24px}
.quote .avatar{flex:0 0 100px;height:100px;border-radius:50%;background:linear-gradient(135deg,#e9e4de,#c8b3a0);border:4px solid var(--white);box-shadow:0 0 0 1px var(--line)}
.quote h3{font-family:"Raleway",sans-serif;font-weight:600;font-size:18px;color:var(--ink);display:flex;justify-content:space-between}
.stars{color:var(--green);letter-spacing:2px}

/* news */
.news{height:360px}
.news .heading{padding-top:30px}
.post{position:absolute;top:120px;width:500px;display:flex;gap:26px}
.post .thumb{flex:0 0 230px;height:210px}
.post h3{font-family:"Raleway",sans-serif;font-weight:600;font-size:24px;color:var(--ink);line-height:1.25}
.post .date{font-size:13px;color:#999;margin:8px 0 18px}
.post .more{display:block;margin-top:14px;color:var(--green);font-size:13px;font-weight:600;text-transform:uppercase}

/* contact */
.contact-sec{height:380px;background:var(--pale)}
.contact-sec .heading{padding-top:30px}
.form{position:absolute;left:70px;top:110px;width:420px}
.row{display:flex;gap:14px;margin-bottom:14px}
.field{flex:1;height:42px;border:1px solid var(--line);background:var(--white);font-size:13px;color:#999;padding:10px 12px}
.field.tall{height:84px}
.form .btn{margin-top:2px}
.details{position:absolute;left:560px;top:120px;font-size:14px;color:var(--text)}
.details li{list-style:none;display:flex;gap:14px;margin-bottom:22px;align-items:flex-start}
.details svg{flex:0 0 18px;margin-top:3px}
.about{position:absolute;left:900px;top:120px;width:240px}
.about .name{font-family:"Raleway",sans-serif;font-weight:700;font-size:18px;color:var(--green);text-transform:uppercase;margin-bottom:14px}
.social{display:flex;gap:12px;margin-top:18px}
.social span{width:34px;height:34px;border-radius:50%;background:var(--green)}

/* footer */
.site-footer{height:100px;background:var(--green);color:var(--white);font-size:14px}
.site-footer .links{position:absolute;left:70px;top:38px;display:flex;gap:30px}
.site-footer .copy{position:absolute;right:70px;top:38px}
</style>
</head>
<body>

<div class="topbar">
  <div class="contact">
    <span><svg width="14" height="11" viewBox="0 0 14 11"><rect x="0.5" y="0.5" width="13" height="10" fill="none" stroke="#fff"/><path d="M1 1l6 5 6-5" fill="none" stroke="#fff"/></svg>hello@silverleafmassage.com</span>
    <span><svg width="12" height="14" viewBox="0 0 12 14"><path d="M2 1h3l1 3-2 1.5c1 2 2 3 3.5 3.5L9 7l3 1v3c0 1-1 2-2 2C5 13 0 8 0 3 0 2 1 1 2 1z" fill="#fff"/></svg>0400 555 218</span>
  </div>
</div>

<header class="site-header">
  <div class="brand"><span class="dot"></span><span class="name">Silverleaf Mobile Massage</span></div>
  <nav class="nav">
    <a class="active">Home</a>
    <a>Services</a>
    <a>Contact</a>
    <a class="jp">ホーム</a>
  </nav>
</header>

<section class="hero" role="img" aria-label="Photo of a woman relaxing during a shoulder massage">
  <div class="hero-text">
    <div class="small">Give yourself</div>
    <div class="mid">A moment of</div>
    <div class="big">Relaxation</div>
    <span class="btn btn-dark">Request an appointment</span>
  </div>
</section>

<section class="welcome">
  <h2 class="heading"><span class="accent">Welcome</span> to Silverleaf Mobile Massage</h2>
  <p class="copy">Lorem Ipsum is simply dummy text of the printing and typesetting industry. Lorem Ipsum has been the industry's standard dummy text ever since the 1500s, when an unknown printer took a galley of type and scrambled it to make a type specimen book. It has survived not only five centuries, but also the leap into electronic typesetting, remaining essentially unchanged. It was popularised in the 1960s.</p>
  <span class="btn btn-green">Read more</span>
  <div class="ph photo" role="img" aria-label="Photo of a relaxed client lying down for a massage with hot stones"></div>
</section>

<section class="services">
  <h2 class="heading"><span class="accent">We offer</span> a wide variety of treatment</h2>
  <div class="tabs">
    <span class="active">Swedish Massage</span>
    <span>Deep Tissue Massage</span>
    <span>Hot Stone Massage</span>
    <span>Other service</span>
  </div>
  <div class="ph photo" role="img" aria-label="Photo of a foot massage with pink flowers"></div>
  <div class="copy">
    <p>Lorem Ipsum is simply dummy text of the printing and typesetting industry. Lorem Ipsum has been the industry's standard dummy text ever since the 1500s, when an unknown printer took a galley of type and scrambled it to make a type specimen book. It has survived not only five centuries, but also the leap into electronic typesetting, remaining essentially unchanged. It was popularised in the 1960s.</p>
    <p>Lorem Ipsum is simply dummy text of the printing and typesetting industry. Lorem Ipsum has been the industry's standard dummy text.</p>
  </div>
</section>

<section class="offer">
  <h2 class="heading">Our special offer</h2>
  <p class="deal">Oil massage 45 min.For only $59.</p>
  <span class="btn btn-white">Book an appointment</span>
</section>

<section class="testimonials">
  <div class="quote" style="left:70px">
    <div class="avatar" role="img" aria-label="Client portrait"></div>
    <div><h3>Client's Name <span class="stars">★★★★★</span></h3>
    <p>Lorem Ipsum is simply dummy text of the printing and typesetting industry. Lorem Ipsum has been the industry's standard dummy text ever since the 1500s.</p></div>
  </div>
  <div class="quote" style="left:660px">
    <div class="avatar" role="img" aria-label="Client portrait"></div>
    <div><h3>Client's Name <span class="stars">★★★★★</span></h3>
    <p>Lorem Ipsum is simply dummy text of the printing and typesetting industry. Lorem Ipsum has been the industry's standard dummy text ever since the 1500s.</p></div>
  </div>
</section>

<section class="news">
  <h2 class="heading"><span class="accent">Latest</span> News</h2>
  <article class="post" style="left:70px">
    <div class="thumb" role="img" aria-label="Photo of a woman enjoying a relaxing treatment" style="background:linear-gradient(135deg,#b98a62,#7a5034)"></div>
    <div><h3>Lorem Ipsum is simply dummy</h3><p class="date">12 Dec 2016</p>
    <p>Lorem Ipsum is simply dummy text of the printing and typesetting.</p><span class="more">Read more »</span></div>
  </article>
  <article class="post" style="left:640px">
    <div class="thumb" role="img" aria-label="Photo of a back massage outdoors" style="background:linear-gradient(135deg,#9fb07a,#5d6e3c)"></div>
    <div><h3>Lorem Ipsum is simply dummy</h3><p class="date">14 Dec 2016</p>
    <p>Lorem Ipsum is simply dummy text of the printing and typesetting.</p><span class="more">Read more »</span></div>
  </article>
</section>

<section class="contact-sec">
  <h2 class="heading"><span class="accent">Contact</span> Us</h2>
  <form class="form">
    <div class="row"><div class="field">Name</div><div class="field">Contact No</div></div>
    <div class="row"><div class="field">E-mail Id</div></div>
    <div class="row"><div class="field tall">Message</div></div>
    <span class="btn btn-green">Submit</span>
  </form>
  <ul class="details">
    <li><svg width="14" height="18" viewBox="0 0 14 18"><path d="M7 0C3 0 0 3 0 7c0 5 7 11 7 11s7-6 7-11c0-4-3-7-7-7zm0 10a3 3 0 110-6 3 3 0 010 6z" fill="#9ccb3b"/></svg><span>123 Lorem Ipsum,<br>Country Zip Code</span></li>
    <li><svg width="14" height="16" viewBox="0 0 12 14"><path d="M2 1h3l1 3-2 1.5c1 2 2 3 3.5 3.5L9 7l3 1v3c0 1-1 2-2 2C5 13 0 8 0 3 0 2 1 1 2 1z" fill="#9ccb3b"/></svg><span>0400 555 218</span></li>
    <li><svg width="16" height="12" viewBox="0 0 14 11"><rect x="0.5" y="0.5" width="13" height="10" fill="none" stroke="#9ccb3b"/><path d="M1 1l6 5 6-5" fill="none" stroke="#9ccb3b"/></svg><span>hello@silverleafmassage.com</span></li>
  </ul>
  <div class="about">
    <div class="name">Silverleaf Mobile Massage</div>
    <p>Lorem Ipsum is simply dummy text of the printing and typesetting.</p>
    <div class="social"><span></span><span></span><span></span><span></span></div>
  </div>
</section>

<footer class="site-footer">
  <div class="links"><span>Home</span><span>Services</span><span>Contact</span></div>
  <div class="copy">© 2016 <strong>SILVERLEAF MOBILE MASSAGE</strong> - All Rights Reserved</div>
</footer>

</body>
</html>
```